Create a Eye Catching Flyerr for my online business

I would like an eye catching flyer with the relevant content for my business.

This flyer is to advertise my online business and the call to action is to get Butchers to sign up to my online site to start selling their products.

the flyer must be eye catching, each to understand, easy to read and relevant to the audience being local butcher shops.

Attached is the marketing packs with all the required information about the business The flyer must not be too long, but the front page must be catching and want the audience to read more. It must very direct, targeted and focused on the audience

It mus be duplicate sides

Reason: need a little more time for review

Industry/Entity Type

Marketing

Font styles to use
Serif
Sans Serif

Colors
9bcb3b
ffffff
fee18a
fac994
f37122
f78f20
ffc214

```html
<!DOCTYPE html>
<html lang="en">
<head>
<meta charset="utf-8">
<title>Cleaver &amp; Catch – Brochure</title>
<link rel="stylesheet" href="https://fonts.googleapis.com/css2?family=Arimo:ital,wght@0,400;0,700;1,700&display=swap">
<style>
  :root{
    --stage-top:#f4f4f4;
    --stage-bottom:#5c6066;
    --green:#5da02e;
    --lime:#9bcb3b;
    --white:#ffffff;
    --note:#fee18a;
    --peach:#fac994;
    --orange:#f37122;
    --amber:#f78f20;
    --gold:#ffc214;
    --navy:#1f3a8f;
    --ink:#1a1a1a;
    --rule:#bdbdbd;
    --label:#ffffff;
    --hub-line:#3f7a20;
  }
  *{box-sizing:border-box;margin:0;padding:0}
  html,body{width:1200px;height:819px;overflow:hidden}
  body{
    position:relative;
    font-family:"Arimo",Arial,sans-serif;
    background:radial-gradient(ellipse at 50% 10%,var(--stage-top) 0%,#c9cacc 45%,var(--stage-bottom) 100%);
  }
  .page{position:absolute;top:61px;width:535px;height:692px;overflow:hidden;box-shadow:0 2px 8px rgba(0,0,0,.35)}
  .page--back{left:47px;background:var(--white)}
  .page--cover{left:602px;background:var(--orange)}
  .page-label{position:absolute;top:772px;color:var(--label);font-size:15px;width:300px;text-align:center}
  .page-label--back{left:156px}
  .page-label--cover{left:729px}

  /* back page */
  .offer-panel{position:absolute;left:0;top:0;width:535px;height:344px;background:var(--green)}
  .join-intro{position:absolute;left:40px;top:38px;width:168px;color:var(--white);font-size:11px;line-height:13.5px}
  .join-intro p{margin-bottom:6px}
  .offer-title{position:absolute;left:241px;top:27px;width:265px;text-align:center;color:var(--white);font-weight:700;font-size:14px;line-height:16.5px}
  .offer-subtitle{position:absolute;left:244px;top:68px;width:250px;text-align:center;color:var(--white);font-weight:700;font-size:15.5px}
  .offer-arrow{position:absolute;left:38px;top:238px}
  .offer-arrow span{position:absolute;left:22px;top:15px;font-weight:700;font-size:16px;color:var(--ink);white-space:nowrap}
  .offer-hub{position:absolute;left:245px;top:80px}
  .hub-text{font-family:"Arimo",Arial,sans-serif;font-size:5.4px;fill:var(--white);text-anchor:middle;font-weight:700}
  .hub-centre-text{font-size:10px}

  .benefits{position:absolute;left:41px;top:395px;list-style:none;width:240px}
  .benefits li{position:relative;padding-left:28px;color:var(--navy);font-weight:700;font-size:13px;line-height:17px;margin-bottom:9px}
  .tick{position:absolute;left:0;top:1px;width:20px;height:20px;background:var(--orange);border:1px solid var(--white);box-shadow:0 0 0 1px var(--orange)}
  .phone{position:absolute;left:325px;top:333px}
  .phone-screen-name{font-family:"Arimo",Arial,sans-serif;font-size:7px;font-weight:700;fill:var(--white);text-anchor:middle}
  .phone-screen-url{font-family:"Arimo",Arial,sans-serif;font-size:6.3px;font-weight:700;fill:var(--ink);text-anchor:middle}
  .divider{position:absolute;left:41px;top:581px;width:455px;height:1px;background:var(--rule)}
  .contact-mark{position:absolute;left:42px;top:592px;width:40px;height:40px;border-radius:50%;background:var(--lime)}
  .contact-mark-name{position:absolute;left:28px;top:634px;width:70px;text-align:center;font-size:6px;font-weight:700;color:var(--ink)}
  .contact{position:absolute;left:105px;top:598px;font-size:10.5px;color:var(--ink);line-height:14px}
  .contact strong{font-style:italic}
  .site-url{position:absolute;left:305px;top:608px;color:var(--amber);font-weight:700;font-size:15px}
  .social{position:absolute;left:353px;top:635px;display:flex;gap:4px}
  .social span{width:20px;height:20px;border-radius:3px;background:#3a76c4}
  .stripe-bar{position:absolute;left:0;top:666px;width:535px;height:26px;display:flex}
  .stripe-bar span{height:100%}

  /* cover page */
  .cover-art{position:absolute;left:0;top:0}
  .sticky-note{position:absolute;left:58px;top:42px;width:196px;height:212px;background:var(--note);transform:rotate(-8deg);box-shadow:3px 6px 10px rgba(0,0,0,.35);padding:20px 10px 0 14px;font-size:11.2px;line-height:15.5px;color:var(--ink)}
  .sticky-tape{position:absolute;left:-12px;top:-10px;width:74px;height:24px;background:rgba(243,113,34,.8);transform:rotate(-14deg)}
  .cover-name{position:absolute;left:150px;top:412px;width:236px;text-align:center;transform:rotate(-24deg);font-weight:700;font-size:17px;color:var(--ink);letter-spacing:.5px}
  .cover-url{position:absolute;left:172px;top:635px;color:var(--white);font-size:18px;text-shadow:0 1px 3px rgba(0,0,0,.6)}
</style>
</head>
<body>

<section class="page page--back">
  <div class="offer-panel">
    <div class="join-intro">
      <p>If you are interested in joining the revolution, the process is very simple.</p>
      <p>Simply send an email to the address below notifying us of that you are interested in signing up along with the package you are interested in. We will contact you with a Insertion form for you to complete.</p>
      <p>In no time you will be ready and advertising online.</p>
    </div>
    <h2 class="offer-title">Cleaver &amp; Catch aim to offer the following to signed up members:</h2>
    <h3 class="offer-subtitle">A world of opportunity</h3>

    <svg class="offer-hub" width="250" height="260" viewBox="0 0 250 260">
      <defs>
        <radialGradient id="g-lime" cx="40%" cy="30%"><stop offset="0" stop-color="#d4ec8a"/><stop offset="1" stop-color="#7fae28"/></radialGradient>
        <radialGradient id="g-green" cx="40%" cy="30%"><stop offset="0" stop-color="#8fd46a"/><stop offset="1" stop-color="#2f8f3a"/></radialGradient>
        <radialGradient id="g-teal" cx="40%" cy="30%"><stop offset="0" stop-color="#8fd8a8"/><stop offset="1" stop-color="#2a8a66"/></radialGradient>
        <radialGradient id="g-blue" cx="40%" cy="30%"><stop offset="0" stop-color="#9fd0e8"/><stop offset="1" stop-color="#2e7ea6"/></radialGradient>
        <radialGradient id="g-navy" cx="40%" cy="30%"><stop offset="0" stop-color="#8aa0e0"/><stop offset="1" stop-color="#2c3e96"/></radialGradient>
        <radialGradient id="g-purple" cx="40%" cy="30%"><stop offset="0" stop-color="#b49ae0"/><stop offset="1" stop-color="#5a3a9a"/></radialGradient>
        <radialGradient id="g-red" cx="40%" cy="30%"><stop offset="0" stop-color="#f08a8a"/><stop offset="1" stop-color="#b21e24"/></radialGradient>
      </defs>
      <g stroke="var(--hub-line)" stroke-width="2">
        <line x1="121" y1="131" x2="121" y2="49"/><line x1="121" y1="131" x2="198" y2="82"/>
        <line x1="121" y1="131" x2="198" y2="175"/><line x1="121" y1="131" x2="121" y2="221"/>
        <line x1="121" y1="131" x2="45" y2="175"/><line x1="121" y1="131" x2="45" y2="82"/>
      </g>
      <circle cx="121" cy="49" r="33" fill="url(#g-lime)" stroke="#fff" stroke-width="1"/>
      <text class="hub-text"><tspan x="121" y="39">Ability to</tspan><tspan x="121" y="46">advertise your</tspan><tspan x="121" y="53">product online</tspan><tspan x="121" y="60">via our site</tspan></text>
      <circle cx="198" cy="82" r="33" fill="url(#g-green)" stroke="#fff" stroke-width="1"/>
      <text class="hub-text"><tspan x="198" y="77">Ability to</tspan><tspan x="198" y="84">manage your</tspan><tspan x="198" y="91">own store portal</tspan></text>
      <circle cx="198" cy="175" r="33" fill="url(#g-teal)" stroke="#fff" stroke-width="1"/>
      <text class="hub-text"><tspan x="198" y="170">Ability to</tspan><tspan x="198" y="177">manage product</tspan><tspan x="198" y="184">listings</tspan></text>
      <circle cx="121" cy="221" r="33" fill="url(#g-blue)" stroke="#fff" stroke-width="1"/>
      <text class="hub-text"><tspan x="121" y="219">Support in</tspan><tspan x="121" y="226">getting started</tspan></text>
      <circle cx="45" cy="175" r="33" fill="url(#g-navy)" stroke="#fff" stroke-width="1"/>
      <text class="hub-text"><tspan x="45" y="163">Ability to</tspan><tspan x="45" y="170">advertising</tspan><tspan x="45" y="177">products with</tspan><tspan x="45" y="184">no payment</tspan><tspan x="45" y="191">functionality</tspan></text>
      <circle cx="45" cy="82" r="33" fill="url(#g-purple)" stroke="#fff" stroke-width="1"/>
      <text class="hub-text"><tspan x="45" y="77">Multiple</tspan><tspan x="45" y="84">payment options</tspan><tspan x="45" y="91">for customers</tspan></text>
      <circle cx="121" cy="131" r="33" fill="url(#g-red)" stroke="#fff" stroke-width="1"/>
      <text class="hub-text hub-centre-text" x="121" y="135">We offer</text>
    </svg>

    <div class="offer-arrow">
      <svg width="182" height="50" viewBox="0 0 182 50">
        <path d="M0 12 H140 V0 L180 25 L140 50 V38 H0 Z" fill="var(--gold)" stroke="#fff36a" stroke-width="1.5"/>
      </svg>
      <span>What We Offer</span>
    </div>
  </div>

  <ul class="benefits">
    <li><span class="tick"><svg width="20" height="20" viewBox="0 0 20 20"><path d="M5 10 L9 14 L15 5" fill="none" stroke="#fff" stroke-width="2.5"/></svg></span>A big point list a product online in 30 secs through your smart phone</li>
    <li><span class="tick"><svg width="20" height="20" viewBox="0 0 20 20"><path d="M5 10 L9 14 L15 5" fill="none" stroke="#fff" stroke-width="2.5"/></svg></span>Don't know how to use a smart phone, full training and support will be available to you anytime</li>
    <li><span class="tick"><svg width="20" height="20" viewBox="0 0 20 20"><path d="M5 10 L9 14 L15 5" fill="none" stroke="#fff" stroke-width="2.5"/></svg></span>No extra employees needed to open up an online shop</li>
  </ul>

  <svg class="phone" width="112" height="272" viewBox="0 0 112 272" role="img" aria-label="Smartphone showing the Cleaver &amp; Catch site">
    <rect x="2" y="2" width="108" height="268" rx="16" fill="#151515"/>
    <rect x="16" y="42" width="80" height="190" fill="var(--amber)"/>
    <circle cx="56" cy="118" r="22" fill="var(--lime)"/>
    <text class="phone-screen-name" x="56" y="150">Cleaver &amp; Catch</text>
    <text class="phone-screen-url" x="56" y="178">CleaverCatch.com.au</text>
    <path d="M50 192 v16 l4 -4 l4 8 l3 -2 l-4 -7 h6 Z" fill="#fff" stroke="#222" stroke-width="1"/>
  </svg>

  <div class="divider"></div>
  <div class="contact-mark"></div>
  <div class="contact-mark-name">Cleaver &amp; Catch</div>
  <div class="contact"><strong>Contact:</strong><br>support@cleavercatch.com.au</div>
  <div class="site-url">CleaverCatch.com.au</div>
  <div class="social" role="img" aria-label="Social media links"><span></span><span></span><span></span></div>

  <div class="stripe-bar">
    <span style="width:80px;background:var(--amber)"></span>
    <span style="width:26px;background:var(--peach)"></span>
    <span style="width:13px;background:var(--gold)"></span>
    <span style="width:14px;background:var(--amber)"></span>
    <span style="width:6px;background:var(--white)"></span>
    <span style="width:44px;background:var(--amber)"></span>
    <span style="width:10px;background:var(--orange)"></span>
    <span style="width:8px;background:var(--amber)"></span>
    <span style="width:139px;background:var(--peach)"></span>
    <span style="width:18px;background:var(--amber)"></span>
    <span style="width:76px;background:var(--green)"></span>
    <span style="width:19px;background:var(--amber)"></span>
    <span style="width:12px;background:var(--white)"></span>
    <span style="width:70px;background:var(--amber)"></span>
  </div>
</section>

<section class="page page--cover">
  <svg class="cover-art" width="535" height="692" viewBox="0 0 535 692">
    <defs>
      <linearGradient id="cover-bg" x1="0" y1="0" x2="0" y2="1"><stop offset="0" stop-color="#f37122"/><stop offset="1" stop-color="#f78f20"/></linearGradient>
      <linearGradient id="meat-photo" x1="0" y1="0" x2="1" y2="1"><stop offset="0" stop-color="#c8343a"/><stop offset="1" stop-color="#7a1a1e"/></linearGradient>
      <linearGradient id="deli-photo" x1="0" y1="0" x2="0" y2="1"><stop offset="0" stop-color="#5a2418"/><stop offset=".5" stop-color="#8a3a30"/><stop offset="1" stop-color="#2a120c"/></linearGradient>
      <radialGradient id="logo-glow"><stop offset=".6" stop-color="#fff"/><stop offset="1" stop-color="#fff" stop-opacity="0"/></radialGradient>
    </defs>
    <rect width="535" height="692" fill="url(#cover-bg)"/>
    <path d="M0 250 C150 215 330 200 535 230 V290 C330 265 160 275 0 320 Z" fill="var(--gold)"/>
    <path d="M0 290 C160 255 330 250 535 275 V305 C340 285 170 300 0 345 Z" fill="#fee18a" opacity=".7"/>
    <rect x="283" y="64" width="235" height="165" rx="20" fill="url(#meat-photo)" role="img" aria-label="Photo of a raw beef cut with herbs, garlic and carrot"/>
    <path d="M0 470 C150 420 330 360 535 350 V692 H0 Z" fill="url(#deli-photo)" role="img" aria-label="Photo of cured sausages, salami and ham"/>
    <path d="M0 470 C150 420 330 360 535 350 V385 C340 390 170 440 0 495 Z" fill="var(--green)"/>
    <circle cx="266" cy="330" r="125" fill="url(#logo-glow)"/>
    <circle cx="266" cy="317" r="92" fill="var(--green)"/>
  </svg>
  <div class="sticky-note">
    <span class="sticky-tape"></span>
    <strong>Selling meat &amp; fish made easy,</strong> get paid orders before you wake up or arrive in the shop, have the money in your bank before the order is picked up or delivered, easiest way to sell your products online, and we do all the hard work for you, cheapest and easiest way to sell your products online with your very own online shop.
  </div>
  <div class="cover-name">CLEAVER &amp; CATCH</div>
  <div class="cover-url">CleaverCatch.com.au</div>
</section>

<div class="page-label page-label--back">Brochure Back</div>
<div class="page-label page-label--cover">Brochure Cover</div>

</body>
</html>
```